Consulting company business cards

We have a base design, but would be willing to update. We have a new logo/"tag" that needs to be added. Current business card design is attached for reference into our "style."

Industry/Entity Type

Business

Contact Information for Business Card

Should contain name and title, office number, mobile number if appropriate, e-mail, website, physical address, and company logo.

Font styles to use
Other font styles liked:
• See current card design on GorvandBCard

Colors
0455a3
85acd3
aaaaaa

Requirements
Must have
• Our colors are navy blue, gray, and a lighter blue
Nice to have
• Design that I can easily drop in new names/titles as we hire employees.

```html
<!DOCTYPE html>
<html lang="en">
<head>
<meta charset="utf-8">
<title>Branwell Business Card</title>
<link href="https://fonts.googleapis.com/css2?family=Roboto+Condensed:wght@400;700&family=Roboto:wght@400&display=swap" rel="stylesheet">
<style>
  :root {
    --page: #eef0f2;
    --card-navy: #1d4560;
    --card-shadow: rgba(10, 30, 45, 0.28);
    --text-white: #f4f6f8;
    --accent-blue: #85acd3;
    --label-gray: #b7c3cd;
    --logo-gray: #dde3e8;
  }
  html, body {
    margin: 0;
    padding: 0;
    width: 1200px;
    height: 903px;
    overflow: hidden;
    background: var(--page);
  }
  .business-card {
    position: absolute;
    left: 100px;
    top: 171px;
    width: 1000px;
    height: 560px;
    background: var(--card-navy);
    border-radius: 28px;
    box-shadow: 0 18px 40px var(--card-shadow);
    font-family: "Roboto Condensed", "Arial Narrow", sans-serif;
    color: var(--text-white);
  }
  .identity {
    position: absolute;
    left: 78px;
    top: 128px;
    padding-left: 32px;
    border-left: 5px solid var(--label-gray);
  }
  .identity-name {
    margin: 0;
    font-size: 40px;
    font-weight: 700;
    letter-spacing: 0.5px;
    line-height: 1.05;
    white-space: nowrap;
  }
  .identity-name .surname { color: var(--accent-blue); }
  .identity-title {
    margin: 4px 0 0;
    font-size: 27px;
    font-weight: 400;
  }
  .brand {
    position: absolute;
    right: 78px;
    top: 112px;
  }
  .brand-row {
    display: flex;
    align-items: center;
    gap: 14px;
  }
  .brand-name {
    font-size: 66px;
    font-weight: 700;
    letter-spacing: 2px;
    line-height: 1;
    color: var(--logo-gray);
  }
  .brand-dot {
    width: 50px;
    height: 50px;
    border-radius: 50%;
    background: var(--accent-blue);
  }
  .brand-tagline {
    margin: 6px 0 0 4px;
    font-family: "Roboto", Arial, sans-serif;
    font-size: 15.5px;
    letter-spacing: 1.6px;
    color: var(--label-gray);
  }
  .contact-list {
    position: absolute;
    left: 84px;
    top: 300px;
    margin: 0;
    padding: 0;
    list-style: none;
    font-size: 26px;
    line-height: 33px;
    white-space: nowrap;
  }
  .contact-label {
    margin-right: 6px;
    font-weight: 700;
    color: var(--label-gray);
  }
  .address {
    position: absolute;
    left: 84px;
    top: 454px;
    margin: 0;
    font-style: normal;
    font-size: 26px;
    line-height: 35px;
    white-space: nowrap;
  }
</style>
</head>
<body>
  <div class="business-card">
    <div class="identity">
      <h1 class="identity-name">DELLA<span class="surname">GORVAND</span></h1>
      <p class="identity-title">Office Manager</p>
    </div>

    <div class="brand">
      <div class="brand-row">
        <span class="brand-name">BRANWELL</span>
        <span class="brand-dot" aria-hidden="true"></span>
      </div>
      <p class="brand-tagline">A CLOUD CONSULTING COMPANY</p>
    </div>

    <ul class="contact-list">
      <li><span class="contact-label">Tel:</span>555.014.2280</li>
      <li><span class="contact-label">Fax:</span>555.014.2291</li>
      <li><span class="contact-label">Email:</span>dgorvand@branwelltech.com</li>
      <li><span class="contact-label">Web:</span>www.branwelltech.com</li>
    </ul>

    <address class="address">1870 N Elmwood Ave, Fairhaven<br>Ohio 43990</address>
  </div>
</body>
</html>
```